Book title: Wildflower: The gift of stillness!

This book is called: Wildflower: The gift of stillness!

A guide to understanding the most popular types of coaching and how to find the perfect coach for you.
The coaching industry has exploded over the past few years as the demand for them has increased. With so many different types of coaches it can be intimidating and overwhelming to find the perfect one for you. To further complicate matters, you may experience times in your life when you require multiple coaches. {Book Title} aims to quite the noise and assist you in finding the perfect coach for you. In this book, you will learn more about the different types of coaching as well as meet a hand-picked selection of coaches from the most popular coaching niches. Each featured coach has provided an exercise designed to move you powerfully forward. We encourage you to work through each exercise so you may experience firsthand the power of working with these incredible coaches.

We would like a professional and simple design. See examples included. We would like to see blood orange included in the design, please see color pallets included as well.

Target Market(s)

Corporate professionals wanting to explore the various types of coaching industry

Industry/Entity Type

Coaching - Health, business, spiritual

Font styles to use
Serif

Colors
EE7325
F08F49
F5BC92
FAE3D3
FDF4ED

Requirements
Must have
• Please include book title: Wildflower, Subtitle: The gift of stillness! Name of publishing company: Silver Lantern Publishing, Spaces for 8 author names on the front of the cover- Author Name
Nice to have
• A feminine yet corporate feel.
Should not have
• We don't want it

```html
<!DOCTYPE html>
<html lang="en">
<head>
<meta charset="utf-8">
<title>Wildflower: The gift of stillness!</title>
<link rel="stylesheet" href="https://fonts.googleapis.com/css2?family=Anton&family=Oswald:wght@300&family=Roboto:wght@400&display=swap">
<style>
  :root {
    --page-bg: #ececec;
    --cover-light: #da6340;
    --cover-mid: #d14f2e;
    --cover-dark: #c1452a;
    --title-white: #ffffff;
    --ink-dark: #250404;
    --rule: rgba(60, 10, 5, 0.55);
    --author-rule: rgba(80, 20, 10, 0.45);
  }
  * { margin: 0; padding: 0; box-sizing: border-box; }
  html, body {
    width: 1084px;
    height: 1200px;
    overflow: hidden;
    background: var(--page-bg);
  }
  .book-cover {
    position: absolute;
    left: 210px;
    top: 40px;
    width: 664px;
    height: 1120px;
    background: linear-gradient(100deg, var(--cover-light) 0%, var(--cover-mid) 45%, var(--cover-dark) 100%);
    box-shadow: 0 10px 30px rgba(0, 0, 0, 0.18);
  }
  .title {
    position: absolute;
    top: 128px;
    left: 0;
    width: 100%;
    text-align: center;
    font-family: "Anton", sans-serif;
    font-size: 118px;
    line-height: 1;
    color: var(--title-white);
    letter-spacing: -1px;
  }
  .connector {
    position: absolute;
    left: 0;
    width: 100%;
    display: flex;
    justify-content: center;
    align-items: center;
    font-family: "Oswald", sans-serif;
    font-weight: 300;
    font-size: 32px;
    line-height: 1;
    color: var(--ink-dark);
  }
  .connector .rule {
    height: 1px;
    background: var(--ink-dark);
  }
  .connector-the { top: 312px; }
  .connector-the .rule { width: 84px; }
  .connector-the .word { margin: 0 8px 0 2px; }
  .connector-of { top: 428px; }
  .connector-of .rule { width: 143px; }
  .connector-of .word { margin: 0 6px; }
  .subtitle-word {
    position: absolute;
    left: 0;
    width: 100%;
    text-align: center;
    font-family: "Anton", sans-serif;
    font-size: 88px;
    line-height: 1;
    color: var(--ink-dark);
  }
  .subtitle-gift { top: 336px; }
  .subtitle-stillness { top: 455px; }
  .author-label {
    position: absolute;
    top: 716px;
    left: 0;
    width: 100%;
    text-align: center;
    font-family: "Roboto", sans-serif;
    font-size: 14px;
    color: var(--ink-dark);
  }
  .author-lines {
    position: absolute;
    top: 740px;
    left: 122px;
    width: 447px;
    height: 190px;
  }
  .author-lines line {
    stroke: var(--author-rule);
    stroke-width: 1;
  }
  .published-label {
    position: absolute;
    top: 958px;
    left: 0;
    width: 100%;
    text-align: center;
    font-family: "Roboto", sans-serif;
    font-size: 14px;
    color: var(--ink-dark);
  }
  .publisher-name {
    position: absolute;
    top: 982px;
    left: 0;
    width: 100%;
    text-align: center;
    font-family: "Roboto", sans-serif;
    font-size: 23px;
    color: var(--title-white);
  }
</style>
</head>
<body>
  <main class="book-cover">
    <h1 class="title">WILDFLOWER</h1>

    <div class="connector connector-the">
      <span class="rule"></span><span class="word">The</span><span class="rule"></span>
    </div>
    <div class="subtitle-word subtitle-gift">GIFT</div>

    <div class="connector connector-of">
      <span class="rule"></span><span class="word">Of</span><span class="rule"></span>
    </div>
    <div class="subtitle-word subtitle-stillness">STILLNESS!</div>

    <p class="author-label">Author:</p>
    <svg class="author-lines" viewBox="0 0 447 190" aria-label="Spaces for author names">
      <line x1="0" y1="3" x2="224" y2="3"/><line x1="236" y1="3" x2="447" y2="3"/>
      <line x1="0" y1="48" x2="224" y2="48"/><line x1="236" y1="48" x2="447" y2="48"/>
      <line x1="0" y1="93" x2="224" y2="93"/><line x1="236" y1="93" x2="447" y2="93"/>
      <line x1="0" y1="138" x2="224" y2="138"/><line x1="236" y1="138" x2="447" y2="138"/>
      <line x1="0" y1="184" x2="224" y2="184"/><line x1="236" y1="184" x2="447" y2="184"/>
    </svg>

    <p class="published-label">Published by :</p>
    <p class="publisher-name">Silver Lantern Publishing.</p>
  </main>
</body>
</html>
```